INTERNATIONAL SPEAKING BUSINESS FOR WOMEN NEEDS A BROCHURE DESIGN

HEARTWARD CIRCLE IS AN INTERNATIONAL FEMALE NETWORK PROVIDING ITS MEMBERS THE UK'S NUMBER ONE RELATIONSHIP SEMINAR FOR WOMEN.
WE ARE ABOUT TO GO LIVE AGAIN AFTER 18 MONTHS AND ONE OF OUR OFFERINGS AT THIS LIVE EVENT, IS OUR CONNECTION GROWTH PROGRAMME - AND THIS IS WHERE YOU COME IN :)
IM LOOKING FOR AN ELEGANT, EASY AND WARM TO THE EYE BROCHURE WHICH CAPTURES SOME OF OUR BEST TESTIMONIALS AND CLIENTS. WE HAVE THE LOGO, THE IMAGES AND THE COPY . WE JUST NEED YOUR AMAZING CREATIVE TALENT AND SKILL TO PUT IT ALL TOGETHER TO LOOK ELEGANT AND PROFESSIONAL, YET WELCOMING AND INSPIRING.
OUR IDEAL CLIENT IS A SINGLE, SUCCESSFUL, PROFESSIONAL WOMAN WANTING TO FIND A SOLUTION TO HER RELATIONSHIP CHALLENGES. SHE WANTS TO LET GO OF HER FEARS OF PAST RELATIONSHIPS AND ALIGN WITH AN AMAZING RELATIONSHIP. OUR AIM WITH THE BROCHURE IS TO SHOW THEM WHAT WE DO, HOW WE DO IT AND HOW OUR EXISTING CLIENTS HAVE ALREADY DONE THIS.
THIS IS JUST ONE OF MANY CREATIVE WORKS NEEDED TO BE CARRIED OUT OVER THESE NEXT FEW WEEKS
SO WE ARE LOOKING FOR OUR IDEAL CREATIVE PARTNER ! HOPING TO FIND YOU HERE ;)
heartwardcircle-example.com
professional, successful women between 30 and 65 looking to resolve their relationship problems
Speaking Business/ Seminars / webinars/ Relationships Coaching for Women
- Similar to logo and website heartwardcircle-example.com

```html
<!DOCTYPE html>
<html lang="en">
<head>
<meta charset="utf-8">
<title>Heartward Circle – Connection Growth Programme Flyer</title>
<link href="https://fonts.googleapis.com/css2?family=Montserrat:wght@400;500;600;700;800&family=Oswald:wght@600;700&display=swap" rel="stylesheet">
<style>
:root{
  --pink:#e5326b;
  --pink-dark:#c9225a;
  --grey:#8a8a8f;
  --grey-dark:#5e5e63;
  --ink:#1d1d22;
  --paper:#f6f6f8;
  --stage:#e9e7ea;
}
*{box-sizing:border-box;margin:0;padding:0}
html,body{width:1200px;height:800px;overflow:hidden;background:var(--stage);font-family:"Montserrat",sans-serif;color:var(--ink)}
.flyer{position:absolute;left:320px;top:6px;width:560px;height:788px;background:var(--paper);box-shadow:0 6px 24px rgba(0,0,0,.18);overflow:hidden}
.brand{position:absolute;left:0;top:0;width:250px;height:74px;background:#fff;display:flex;align-items:center;gap:10px;padding-left:22px}
.brand-dot{width:22px;height:22px;border-radius:50%;background:var(--pink)}
.brand-name{font-family:"Oswald",sans-serif;font-weight:600;font-size:19px;color:var(--pink);letter-spacing:.3px}
.intro{position:absolute;left:0;top:74px;width:262px;height:124px;background:var(--pink);color:#fff;font-weight:700;font-size:11px;line-height:1.35;padding:10px 14px 0 22px}
.hero{position:absolute;left:250px;top:0;width:310px;height:262px;background:linear-gradient(160deg,#d9d4d8 0%,#a8909a 40%,#5a3f48 70%,#b6646f 100%);clip-path:polygon(0 0,100% 0,100% 100%,22% 100%)}
.included{position:absolute;left:0;top:198px;width:275px;padding:12px 16px 0 22px}
.included h2,.section h2{font-weight:800;font-size:14.5px;margin-bottom:7px}
.included ol{list-style:none}
.included li{display:flex;gap:8px;font-size:9.5px;font-weight:500;line-height:1.3;margin-bottom:7px}
.num{flex:none;width:17px;height:17px;border-radius:50%;border:1.5px solid var(--pink);color:var(--pink);font-size:9px;font-weight:700;display:flex;align-items:center;justify-content:center}
.about{position:absolute;left:0;top:302px;width:290px;height:84px;background:var(--grey);color:#fff;padding:11px 16px 0 22px}
.about h2{font-weight:800;font-size:14px;margin-bottom:5px}
.about p{font-size:10px;line-height:1.35}
.schedule{position:absolute;left:290px;top:262px;width:270px;height:46px;background:var(--pink);color:#fff;font-family:"Oswald",sans-serif;font-weight:700;font-size:27px;display:flex;align-items:center;justify-content:center;letter-spacing:.3px}
.schedule-rule{position:absolute;left:290px;top:308px;width:270px;height:14px;background:var(--grey)}
.section{position:absolute;left:22px;width:516px}
.fit{top:398px}
.fit p{font-size:10px;line-height:1.4;font-weight:500}
.learn{top:474px}
.learn-grid{display:grid;grid-template-columns:1fr 1fr;gap:14px}
.learn ul{list-style:none}
.learn li{position:relative;padding-left:14px;font-size:9.5px;font-weight:500;line-height:1.32;margin-bottom:8px}
.learn li::before{content:"";position:absolute;left:0;top:3px;width:8px;height:8px;border-radius:50%;background:var(--pink)}
.price{position:absolute;left:330px;top:566px;width:198px;border:1.5px solid var(--pink);background:#fff;text-align:center}
.price-label{background:var(--pink);color:#fff;font-weight:800;font-size:15px;padding:3px 0;letter-spacing:.4px}
.price-value{font-weight:800;font-size:17px;padding:3px 0 5px}
.cta{position:absolute;left:0;top:624px;width:560px;height:116px;background:#fff;padding:8px 22px 0}
.cta h2{color:var(--pink);font-weight:800;font-size:19px;margin-bottom:3px}
.cta h3{font-weight:800;font-size:13px;line-height:1.3;margin-bottom:5px}
.cta p{font-size:9.5px;font-weight:500;line-height:1.4}
.footer{position:absolute;left:0;bottom:0;width:560px;height:48px;background:var(--grey-dark);color:#fff;display:flex;align-items:center;justify-content:space-between;padding:0 22px;font-size:9.5px;font-weight:500}
.contact{display:flex;align-items:center;gap:6px}
.contact svg{width:12px;height:12px;fill:var(--pink)}
</style>
</head>
<body>
<main class="flyer">
  <header class="brand">
    <span class="brand-dot"></span>
    <span class="brand-name">HEARTWARD CIRCLE</span>
  </header>
  <p class="intro">Immerse yourself with a group of likeminded individuals in a weekly masterclass and get absorbed in some of the most senior relationships content that's changing the lives of thousands of women internationally.</p>
  <div class="hero" role="img" aria-label="Photo of a speaker presenting to a seated audience in front of a projection screen"></div>

  <section class="included">
    <h2>What's Included:</h2>
    <ol>
      <li><span class="num">1</span><span>Receive full access to the Masterclasses Series Programme (once a week)</span></li>
      <li><span class="num">2</span><span>Gain full access to the network via our private Circlespace group.</span></li>
    </ol>
  </section>
  <section class="about">
    <h2>About The Masterclass:</h2>
    <p>Immerse yourself for one hour a week with like-minded individuals from the comfort and safety of your own home.</p>
  </section>

  <div class="schedule">Mondays 7pm-8pm</div>
  <div class="schedule-rule"></div>

  <section class="section fit">
    <h2>Is this programme for me?</h2>
    <p>If you wish to Join one of the UK's Top Female Networks for a Life Changing Year but the unlimited programme is out of budget, then the Masterclass programme is for you. Give yourself that step in between, the CONNECTION GROWTH PROGRAMME. We've packaged it up so that you can afford it!</p>
  </section>

  <section class="section learn">
    <h2>What will I learn/ get from the programme?</h2>
    <div class="learn-grid">
      <ul>
        <li>Weekly opportunity to have all your burning relationship questions answered</li>
        <li>Immerse with a powerful network of like-minded women and learn even more</li>
      </ul>
      <ul>
        <li>Tools to help you overcome past relationship wounds and patterns</li>
        <li>Deepen your understanding of self-mastery on route to relationship Mastery</li>
      </ul>
    </div>
  </section>

  <section class="cta">
    <h2>Don't let today finish here.</h2>
    <h3>Register today and<br>get the first months' worth TODAY.</h3>
    <p>Tomorrow, wake up and watch half a day of the most powerful content for relationships out there. That's half a day of advanced content for only £200.<br>If at any point you wish to cancel your subscription, just give us 30 days notice.</p>
  </section>

  <aside class="price">
    <div class="price-label">SUBSCRIPTION:</div>
    <div class="price-value">£200 a month</div>
  </aside>

  <footer class="footer">
    <span class="contact"><svg viewBox="0 0 24 24"><path d="M6.6 10.8a15 15 0 0 0 6.6 6.6l2.2-2.2a1 1 0 0 1 1-.25 11.4 11.4 0 0 0 3.6.6 1 1 0 0 1 1 1V20a1 1 0 0 1-1 1A17 17 0 0 1 3 4a1 1 0 0 1 1-1h3.5a1 1 0 0 1 1 1c0 1.25.2 2.45.6 3.6a1 1 0 0 1-.25 1z"/></svg>+44 20 7946 0321</span>
    <span class="contact"><svg viewBox="0 0 24 24"><path d="M2 5h20v14H2zm2 2v.5l8 5 8-5V7z"/></svg>contact@heartwardcircle-example.com</span>
    <span class="contact"><svg viewBox="0 0 24 24"><circle cx="12" cy="12" r="10"/></svg>www.heartwardcircle-example.com</span>
  </footer>
</main>
</body>
</html>
```